Copper Lantern - responsive bootstrap website design

Looking to build a responsive service website.

Logo has been provided.

PLEASE REVIEW ATTACHED DESIGN STYLE GUIDES & CLIENT CREATIVE BRIEF FOR OUR REQUIREMENT.

THANK YOU AND GOOD LUCK!

Industry/Entity Type

Build

```html
<!DOCTYPE html>
<html lang="en">
<head>
<meta charset="utf-8">
<title>Copper Lantern Outfitters</title>
<link href="https://fonts.googleapis.com/css2?family=Arimo:wght@400;700&display=swap" rel="stylesheet">
<style>
  :root {
    --bar: #1b1b1b;
    --teal: #0e7a6a;
    --teal-dark: #0a5e52;
    --text: #555555;
    --heading: #333333;
    --white: #ffffff;
    --sand: #d4d2a0;
    --sea-top: #2a4a86;
    --sea-bottom: #142a5a;
    --sunset-sky: #8a8c96;
    --sunset-glow: #e0683a;
    --notch: #9c9c8c;
  }
  * { box-sizing: border-box; margin: 0; padding: 0; }
  html, body { width: 676px; height: 1200px; overflow: hidden; }
  body {
    font-family: "Arimo", Helvetica, Arial, sans-serif;
    background: var(--white);
    color: var(--text);
    position: relative;
  }
  .site-header {
    height: 58px;
    background: var(--bar);
    position: relative;
    z-index: 2;
  }
  .brand {
    position: absolute;
    left: 34px; top: 0;
    width: 210px; height: 91px;
    background: var(--teal);
    border: 1px solid var(--teal-dark);
    box-shadow: 0 2px 4px rgba(0,0,0,.35);
    display: flex; align-items: center; justify-content: center;
    text-align: center;
    color: var(--white);
    font-size: 21px;
    line-height: 1.15;
    font-weight: 400;
  }
  .menu-toggle {
    position: absolute;
    right: 18px; top: 15px;
    width: 32px; height: 32px;
    background: #2e2e2e;
    border: 1px solid #3a3a3a;
    display: flex; align-items: center; justify-content: center;
  }
  .hero {
    height: 238px;
    background: linear-gradient(180deg, var(--sea-top), var(--sea-bottom));
    position: relative;
  }
  .hero-dots {
    position: absolute; left: 4px; bottom: 6px;
    display: flex; gap: 4px;
  }
  .hero-dots span { width: 6px; height: 6px; background: #ddd; }
  .hero-dots span + span { background: #555; }
  .about {
    height: 250px;
    text-align: center;
    padding: 24px 56px 0;
  }
  .about h1 {
    color: var(--teal);
    font-weight: 400;
    font-size: 39px;
    line-height: 1;
    margin-bottom: 22px;
  }
  .about p {
    font-size: 17px;
    line-height: 26.4px;
  }
  .services-banner {
    height: 114px;
    background: linear-gradient(180deg, var(--sunset-sky) 0%, #b0a8a4 45%, var(--sunset-glow) 75%, #3a4454 100%);
    display: flex; align-items: center; justify-content: center;
  }
  .services-banner h2 {
    color: var(--white);
    font-weight: 400;
    font-size: 38px;
    text-shadow: 0 2px 3px rgba(0,0,0,.7);
  }
  .services {
    position: relative;
    background: var(--sand);
    height: 540px;
    padding: 48px 60px 0;
    text-align: center;
  }
  .services .notch {
    position: absolute; left: 312px; top: 0;
  }
  .service { margin-bottom: 37px; }
  .service h3 {
    color: var(--heading);
    font-size: 18px;
    font-weight: 700;
    margin-bottom: 10px;
  }
  .service p {
    color: var(--heading);
    font-size: 14.6px;
    line-height: 26.4px;
    margin-bottom: 19px;
  }
  .read-more {
    display: inline-block;
    background: var(--teal);
    color: var(--white);
    font-size: 14px;
    line-height: 26px;
    padding: 0 9px;
    border-radius: 2px;
    text-decoration: none;
  }
</style>
</head>
<body>
  <header class="site-header">
    <div class="brand">Copper Lantern<br>Outfitters</div>
    <div class="menu-toggle">
      <svg width="16" height="14" viewBox="0 0 16 14"><rect y="0" width="16" height="2.5" fill="#0e7a6a"/><rect y="5.5" width="16" height="2.5" fill="#0e7a6a"/><rect y="11" width="16" height="2.5" fill="#0e7a6a"/></svg>
    </div>
  </header>

  <section class="hero" role="img" aria-label="Angler on the open sea holding up a large silver fish">
    <div class="hero-dots"><span></span><span></span></div>
  </section>

  <section class="about">
    <h1>ABOUT US</h1>
    <p>We offer you a very unique fishing experience which is challenging, amid a beautiful setting. Near Atlantic coast beaches and surrounded by beautiful marsh views, Hilton Head Island is situated in a wonderful community in peaceful solitude with Live Oaks draped in Spanish Moss.</p>
  </section>

  <section class="services-banner" role="img" aria-label="Sunset over the marsh with a dock">
    <h2>GUIDE SERVICES</h2>
  </section>

  <section class="services">
    <svg class="notch" width="52" height="16" viewBox="0 0 52 16"><polygon points="0,0 52,0 26,16" fill="var(--notch)"/></svg>
    <article class="service">
      <h3>Inshore Fishing</h3>
      <p>Lorem ipsum dolor sit amet, consectetuer adipiscing elit, sed diam nonummy nibh euismod tincidunt ut laoreet dolore magna aliquam erat volutpat. Ut wisi enim ad minim veniam, quis nostrud exerci tation ullamcorper suscipit lobortis nisl ut aliquip ex ea commodo consequat.</p>
      <a class="read-more" href="#">read more ...</a>
    </article>
    <article class="service">
      <h3>Inshore Fishing</h3>
      <p>Lorem ipsum dolor sit amet, consectetuer adipiscing elit, sed diam nonummy nibh euismod tincidunt ut laoreet dolore magna aliquam erat volutpat. Ut wisi enim ad minim veniam, quis nostrud exerci tation ullamcorper suscipit lobortis nisl ut aliquip ex ea commodo consequat.</p>
      <a class="read-more" href="#">read more ...</a>
    </article>
  </section>
</body>
</html>
```